List Now, Launch Later - DL Flyer front & back

Looking for a flyer that has nothing much other than “List Now, Launch Later” on the front with text to fill the back. With image on front that symbolises launch, maybe house being launch like a rocket.
The text has yet to be written but here is the gist: This is for the back of flyer.
List property and delay the launch. In the meantime, we can:
· Prepare contract
· Prepare marketing
· Prepare the property
· Do the Pest and Building Report
· Give the tenants their due notice of sale
· Advise buyers in an off market capacity
This ensures we are first to market when the time comes rather than coming onto the market along with a surge of spring sellers. Buyers are still buying now. The lack of stock is inadvertently creating strength in the market.
The feel has to be modern, clean, contemporary & graphic

```html
<!DOCTYPE html>
<html lang="en">
<head>
<meta charset="utf-8">
<title>List Now, Launch Later – Flyer Front</title>
<link rel="stylesheet" href="https://fonts.googleapis.com/css2?family=Montserrat:wght@800&display=swap">
<style>
  :root {
    --ink: #0a0a0a;
    --accent: #f9ad3c;
    --veil: rgba(255, 255, 255, 0.55);
    --photo-light: #ecebe9;
    --photo-mid: #c9c7c4;
    --photo-wood: #9a6a45;
    --mark-grey: #7a7a7a;
  }
  * { margin: 0; padding: 0; box-sizing: border-box; }
  html, body { width: 848px; height: 1200px; overflow: hidden; background: #fff; }
  .flyer {
    position: relative;
    width: 848px;
    height: 1200px;
    overflow: hidden;
    font-family: "Montserrat", sans-serif;
  }
  .interior-photo {
    position: absolute;
    inset: 0;
    background:
      linear-gradient(180deg, var(--photo-light) 0%, #f2f2f1 45%, var(--photo-mid) 72%, #d8d6d3 88%, var(--photo-wood) 100%);
  }
  .veil-main {
    position: absolute;
    left: 71px;
    top: 0;
    width: 777px;
    height: 1100px;
    background: var(--veil);
  }
  .veil-foot {
    position: absolute;
    left: 376px;
    top: 1100px;
    width: 472px;
    height: 100px;
    background: var(--veil);
  }
  .launch-mark {
    position: absolute;
    left: 190px;
    top: 212px;
    width: 289px;
    height: 288px;
    border-radius: 40px;
    background: linear-gradient(135deg, var(--mark-grey) 0%, #9a9a9a 60%, var(--accent) 100%);
    opacity: 0.85;
  }
  .rule {
    position: absolute;
    left: 190px;
    top: 700px;
    width: 168px;
    height: 4px;
    background: var(--accent);
  }
  .headline {
    position: absolute;
    left: 186px;
    top: 756px;
    font-size: 71px;
    font-weight: 800;
    line-height: 77px;
    letter-spacing: -0.5px;
    color: var(--ink);
    text-transform: uppercase;
  }
  .next-arrow {
    position: absolute;
    left: 757px;
    top: 910px;
  }
</style>
</head>
<body>
<main class="flyer">
  <div class="interior-photo" role="img" aria-label="Bright modern living room with white sofa, laptop on glass table, fireplace and wooden floor"></div>
  <div class="veil-main"></div>
  <div class="veil-foot"></div>

  <div class="launch-mark" role="img" aria-label="Graphic of a house shape launching like a rocket with an orange flame"></div>

  <div class="rule"></div>
  <h1 class="headline">List now,<br>launch<br>later.</h1>

  <svg class="next-arrow" width="35" height="65" viewBox="0 0 35 65" aria-hidden="true">
    <polygon points="0,0 35,32.5 0,65" fill="var(--accent)"/>
  </svg>
</main>
</body>
</html>
```